need professional, precise design for a website

I will start with a homepage design and if we pick your design, we'll have you design up to 6 more interior pages (we'll pay extra for these of course). We need a homepage design for a reserve study company based in Idaho, covering the northwest region. The company is called copper ridge reserve study. Their current site is at https://www.copperridgereserves.example/ and they really like this site for inspiration https://www.fundplannerhub.example/ but they would like an original design, just more modern and fresh like the sample site. I have logo files I will attach. They want something that looks financial and has a feel of accuity. Their main call to action will be to have someone fill in a contact form or call them on the phone. They will have a sample study that someone can download as on the fundplannerhub site. You can use copy from their current site.

```html
<!DOCTYPE html>
<html lang="en">
<head>
<meta charset="utf-8">
<title>Copper Ridge Reserves — Reserve Studies</title>
<link href="https://fonts.googleapis.com/css2?family=Cormorant+Garamond:wght@500;600;700&family=Lato:wght@400;700&display=swap" rel="stylesheet">
<style>
:root{
  --navy:#1f2566;
  --ink:#222;
  --muted:#666;
  --light:#f4f4f4;
  --line:#dcdcdc;
  --dark:#121212;
  --white:#fff;
  --hero-a:#2d3a4f;
}
*{margin:0;padding:0;box-sizing:border-box}
html,body{width:1200px;height:4128px;overflow:hidden}
body{position:relative;background:var(--white);font-family:'Lato',sans-serif;color:var(--ink)}
section,header,footer{position:absolute;left:0;width:1200px}

/* header */
.site-header{top:0;height:105px;background:var(--white)}
.brand{position:absolute;left:83px;top:30px;display:flex;align-items:center;gap:10px;font-family:'Cormorant Garamond',serif;font-weight:600;font-size:26px;color:var(--navy)}
.brand-dot{width:16px;height:16px;border-radius:50%;background:var(--navy)}
.main-nav{position:absolute;left:627px;top:44px;display:flex;gap:30px;font-size:14px;letter-spacing:.5px;color:#555;text-transform:uppercase}
.main-nav .active{color:var(--navy)}

/* hero */
.hero{top:105px;height:550px;background:linear-gradient(180deg,#3d4a5e 0%,var(--hero-a) 55%,#1e2733 100%)}
.hero-title{position:absolute;top:210px;width:100%;text-align:center;color:var(--white);font-family:'Cormorant Garamond',serif;font-weight:500;font-size:46px;line-height:1.3;letter-spacing:1px;text-transform:uppercase}
.slider-dots{position:absolute;right:36px;top:232px;display:flex;flex-direction:column;gap:9px}
.slider-dots span{width:13px;height:13px;border-radius:50%;border:2px solid var(--white)}
.slider-dots span.on{background:var(--white)}

/* welcome */
.welcome{top:655px;height:495px}
.welcome .photo{position:absolute;top:88px;width:231px;height:314px}
.photo-a{left:77px;background:linear-gradient(160deg,#c9d2dc,#5b6c80)}
.photo-b{left:327px;background:linear-gradient(180deg,#8aa3a0 0%,#6f8a4e 60%,#4f7a2c 100%)}
.welcome h2{position:absolute;left:638px;top:104px;font-family:'Cormorant Garamond',serif;font-weight:700;font-size:33px;line-height:1.15;color:var(--navy);text-transform:uppercase;letter-spacing:1px}
.welcome .copy{position:absolute;left:638px;top:200px;width:480px;font-size:13.5px;line-height:1.75;color:var(--muted)}
.welcome .copy p+p{margin-top:14px}

/* reserve studies */
.studies{top:1150px;height:446px;background:var(--light)}
.section-title{position:absolute;width:100%;text-align:center;font-family:'Cormorant Garamond',serif;font-weight:700;font-size:31px;color:var(--navy);text-transform:uppercase;letter-spacing:1px}
.studies .section-title{top:34px}
.study-line{position:absolute;top:151px;left:260px;width:680px;height:1px;background:var(--line)}
.study{position:absolute;top:102px;width:250px;margin-left:-125px;text-align:center}
.study .icon{width:100px;height:100px;margin:0 auto;border-radius:50%;background:var(--white);display:flex;align-items:center;justify-content:center}
.study h3{margin-top:38px;font-family:'Cormorant Garamond',serif;font-weight:700;font-size:21px;color:var(--navy);text-transform:uppercase;letter-spacing:.5px;white-space:nowrap}
.study p{margin:10px auto 0;width:205px;height:63px;font-size:13px;line-height:1.6;color:var(--muted)}
.read-more{margin-top:16px;display:inline-flex;align-items:center;gap:8px;font-family:'Cormorant Garamond',serif;font-weight:700;font-size:14px;color:var(--navy);text-transform:uppercase}

/* planning band */
.planning{top:1596px;height:551px;background:linear-gradient(120deg,#3b4f6e 0%,#5d7390 45%,#8a7560 100%)}
.planning-box{position:absolute;left:77px;top:96px;width:476px;height:372px;background:rgba(28,32,40,.9);padding:40px 32px;color:var(--white);text-align:center}
.planning-box h2{font-family:'Cormorant Garamond',serif;font-weight:700;font-size:27px;line-height:1.3}
.planning-box p{margin-top:18px;font-size:13px;line-height:1.8;color:#e6e6e6}

/* blog */
.blog{top:2147px;height:605px}
.blog .section-title{top:50px}
.post{position:absolute;top:110px;width:325px;height:407px;border:1px solid #e2e2e2;background:var(--white)}
.post .thumb{height:206px}
.thumb-1{background:linear-gradient(135deg,#c7d3de,#6a86a6)}
.thumb-2{background:linear-gradient(180deg,#7e8a96,#4d5663)}
.thumb-3{background:linear-gradient(180deg,#2e3d6e 0%,#7a6b8f 60%,#1d2238 100%)}
.post h3{margin:22px 18px 0;font-size:17px;font-weight:400;line-height:1.45;color:var(--ink)}
.post p{margin:14px 18px 0;font-size:13px;line-height:1.7;color:var(--muted)}

/* testimonials */
.testimonials{top:2752px;height:606px;background:var(--light)}
.testimonials .section-title{top:50px}
.quote-card{position:absolute;left:308px;top:138px;width:584px;height:261px;background:var(--white);padding:48px 50px;text-align:center;font-size:13px;line-height:1.8;color:var(--muted)}
.avatar{position:absolute;left:556px;top:355px;width:88px;height:88px;border-radius:50%;background:linear-gradient(180deg,#6d7c8a,#3c4752)}
.client{position:absolute;top:468px;width:100%;text-align:center}
.client strong{display:block;font-size:16px;font-weight:400;letter-spacing:1px;color:#333}
.client span{display:block;margin-top:12px;font-size:14px;color:var(--muted)}

/* contact */
.contact{top:3358px;height:687px;background:var(--dark);color:var(--white)}
.contact-info{position:absolute;left:77px;top:108px;width:500px}
.contact-info h2{font-family:'Cormorant Garamond',serif;font-weight:600;font-size:33px;text-transform:uppercase;letter-spacing:1px}
.contact-info .tag{margin-top:16px;font-size:16px;color:#ddd}
.info-row{display:flex;gap:24px;padding:34px 0;border-bottom:1px solid #333}
.info-row:last-child{border-bottom:none}
.info-row h4{font-size:17px;font-weight:400;text-transform:uppercase;letter-spacing:.5px}
.info-row p{margin-top:8px;font-size:12.5px;color:#ccc}
.form-card{position:absolute;left:644px;top:90px;width:479px;height:501px;background:var(--white);border-radius:6px;padding:46px 42px;color:var(--ink)}
.form-card h3{font-family:'Cormorant Garamond',serif;font-weight:700;font-size:21px;text-transform:uppercase;letter-spacing:.5px}
.field{margin-top:12px;height:48px;border:1px solid #ccc;padding:14px 12px;font-size:12px;color:#888}
.form-card .field:first-of-type{margin-top:24px}
.field.message{height:94px}
.send{margin-top:22px;width:160px;height:48px;background:#0d0d0d;color:var(--white);border:none;font-family:'Cormorant Garamond',serif;font-weight:700;font-size:18px;letter-spacing:1px}
.copyright{top:4045px;height:83px;display:flex;align-items:center;justify-content:center;font-size:12px;color:#666}
</style>
</head>
<body>

<header class="site-header">
  <div class="brand"><span class="brand-dot"></span>Copper Ridge Reserves</div>
  <nav class="main-nav">
    <span class="active">Home</span><span>About Our Company</span><span>Reserve Studies</span><span>Contact Us</span>
  </nav>
</header>

<section class="hero" role="img" aria-label="City skyline with office towers under an overcast sky">
  <h1 class="hero-title">Your Financial Road Map<br>for the Next 30 Years!</h1>
  <div class="slider-dots"><span class="on"></span><span></span><span></span><span></span></div>
</section>

<section class="welcome">
  <div class="photo photo-a" role="img" aria-label="Modern glass office building"></div>
  <div class="photo photo-b" role="img" aria-label="Community park playground on a lawn"></div>
  <h2>Welcome to<br>Copper Ridge Reserves</h2>
  <div class="copy">
    <p>A mountain ridge is a constant on the horizon that travelers have relied on for generations. Finding your way is simply knowing the right points of origin and following the trail the landscape has laid before us.</p>
    <p>We love the high country! Amidst so many valleys and a seemingly endless expanse of peaks and passes, there is great order. Of all the summits and distractions of the wide open land, the ridge line remains ever true, ever steady and ever rooted. A financial plan should be equally so!</p>
  </div>
</section>

<section class="studies">
  <h2 class="section-title">Reserve Studies</h2>
  <div class="study-line"></div>
  <div class="study" style="left:200px">
    <div class="icon"><svg width="44" height="44" viewBox="0 0 44 44" fill="none" stroke="#1f2566" stroke-width="2"><rect x="5" y="12" width="28" height="18" rx="2"/><circle cx="19" cy="21" r="4"/><rect x="11" y="18" width="28" height="18" rx="2" fill="#fff"/><circle cx="25" cy="27" r="4"/></svg></div>
    <h3>HOA Reserves</h3>
    <p>Every homeowners association is different. Different sets of assets, different financials...</p>
    <div class="read-more">Read More <svg width="24" height="12" viewBox="0 0 24 12" fill="none" stroke="#1f2566" stroke-width="2"><path d="M0 6h22M17 1l5 5-5 5"/></svg></div>
  </div>
  <div class="study" style="left:465px">
    <div class="icon"><svg width="44" height="44" viewBox="0 0 44 44" fill="none" stroke="#1f2566" stroke-width="2"><rect x="8" y="6" width="18" height="32"/><rect x="26" y="16" width="10" height="22"/><path d="M13 12h3M19 12h3M13 18h3M19 18h3M13 24h3M19 24h3M15 38v-6h4v6"/></svg></div>
    <h3>Condo Reserves</h3>
    <p>Each of these is taken into consideration to customize your 30 year budget and build...</p>
    <div class="read-more">Read More <svg width="24" height="12" viewBox="0 0 24 12" fill="none" stroke="#1f2566" stroke-width="2"><path d="M0 6h22M17 1l5 5-5 5"/></svg></div>
  </div>
  <div class="study" style="left:735px">
    <div class="icon"><svg width="44" height="44" viewBox="0 0 44 44" fill="none" stroke="#1f2566" stroke-width="2"><rect x="10" y="8" width="24" height="30"/><path d="M15 14h4M25 14h4M15 20h4M25 20h4M15 26h4M25 26h4M19 38v-6h6v6M6 38h32"/></svg></div>
    <h3>Hotel, Hospitals</h3>
    <p>Every homeowners association is different. Different sets of assets, different financials...</p>
    <div class="read-more">Read More <svg width="24" height="12" viewBox="0 0 24 12" fill="none" stroke="#1f2566" stroke-width="2"><path d="M0 6h22M17 1l5 5-5 5"/></svg></div>
  </div>
  <div class="study" style="left:1002px">
    <div class="icon"><svg width="44" height="44" viewBox="0 0 44 44" fill="none" stroke="#1f2566" stroke-width="2"><circle cx="22" cy="22" r="15"/><ellipse cx="22" cy="22" rx="7" ry="15"/><path d="M7 22h30M9 15h26M9 29h26"/></svg></div>
    <h3>Parks &amp; Public Lands</h3>
    <p>Much like HOA's and condominiums, you have finite funds that originate...</p>
    <div class="read-more">Read More <svg width="24" height="12" viewBox="0 0 24 12" fill="none" stroke="#1f2566" stroke-width="2"><path d="M0 6h22M17 1l5 5-5 5"/></svg></div>
  </div>
</section>

<section class="planning" role="img" aria-label="Modern condominium building with balconies against a blue sky">
  <div class="planning-box">
    <h2>Prior Proper Planning Prevents<br>Poor Performance!</h2>
    <p>It's not just a catchy phrase, it's our motto! The great strategist and creative thinker, Elias Marlow, said "If you fail to plan, you are planning to fail!"</p>
    <p>Life delivers enough failures and shortfalls! Don't let your budget, your buildings or your financials, fall short of expectations. We will help you plan, strategize and prepare your property for the next 30 years. It's not quite a crystal ball but it is the Copper Ridge!</p>
  </div>
</section>

<section class="blog">
  <h2 class="section-title">Latest Blog</h2>
  <article class="post" style="left:77px">
    <div class="thumb thumb-1" role="img" aria-label="Team reviewing financial charts together"></div>
    <h3>Lorem Ipsum is simply dummy text of the printing and typesetting.</h3>
    <p>Lorem Ipsum is simply dummy text of the printing and typesetting industry. Lorem Ipsum has been the industry's standard dum.</p>
  </article>
  <article class="post" style="left:438px">
    <div class="thumb thumb-2" role="img" aria-label="Office building facade with many windows"></div>
    <h3>Lorem Ipsum is simply dummy text of the printing and typesetting.</h3>
    <p>Lorem Ipsum is simply dummy text of the printing and typesetting industry. Lorem Ipsum has been the industry's standard dum.</p>
  </article>
  <article class="post" style="left:798px">
    <div class="thumb thumb-3" role="img" aria-label="City skyline at dusk"></div>
    <h3>Lorem Ipsum is simply dummy text of the printing and typesetting.</h3>
    <p>Lorem Ipsum is simply dummy text of the printing and typesetting industry. Lorem Ipsum has been the industry's standard dum.</p>
  </article>
</section>

<section class="testimonials">
  <h2 class="section-title">Testimonias</h2>
  <div class="quote-card">Lorem Ipsum is simply dummy text of the printing and typesetting industry. Lorem Ipsum has been the industry's standard dummy text ever since the 1500s, when an unknown printer took a galley of type and scrambled it to make a type specimen book. It has survived not only five centuries, but also the leap into electronic typesetting, remaining essentially unchanged.</div>
  <div class="avatar" role="img" aria-label="Client portrait"></div>
  <div class="client"><strong>NAME SURNAME</strong><span>Lorem Ipsum is simply dummy text.</span></div>
</section>

<footer class="contact">
  <div class="contact-info">
    <h2>Contact Info</h2>
    <p class="tag">Your financial road map for the next 30 years!</p>
    <div class="info-row">
      <svg width="40" height="40" viewBox="0 0 40 40" fill="none" stroke="#fff" stroke-width="2"><path d="M20 34s-10-10-10-18a10 10 0 0 1 20 0c0 8-10 18-10 18z"/><circle cx="20" cy="16" r="4"/><path d="M6 30l-3 7h34l-3-7"/></svg>
      <div><h4>Location</h4><p>Serving communities across the Northwest &amp; Mountain West</p></div>
    </div>
    <div class="info-row">
      <svg width="40" height="40" viewBox="0 0 40 40" fill="none" stroke="#fff" stroke-width="2"><rect x="3" y="6" width="34" height="28" rx="4"/><path d="M13 12c-2 2-1 7 4 12s10 6 12 4l-3-4-3 2c-2-1-5-4-6-6l2-3z"/></svg>
      <div><h4>Phone</h4><p>(555) 010-0142</p></div>
    </div>
    <div class="info-row">
      <svg width="40" height="40" viewBox="0 0 40 40" fill="none" stroke="#fff" stroke-width="2"><rect x="4" y="12" width="32" height="24"/><path d="M4 12l16 13 16-13M10 12V4h20v8M14 10h12M14 15h12"/></svg>
      <div><h4>Email</h4><p>hello@copperridgereserves.example</p></div>
    </div>
  </div>
  <div class="form-card">
    <h3>Get in Touch With Us</h3>
    <div class="field">Name</div>
    <div class="field">Email</div>
    <div class="field">Phone</div>
    <div class="field message">Message</div>
    <button class="send">SEND</button>
  </div>
</footer>

<footer class="copyright">©COPPER RIDGE RESERVES- 2019. All Rights Reserved</footer>

</body>
</html>
```